World first health care product in tablet form to help save relationships and marriages

The product known as Zentharo is in tablet form 470mg and has 30 to a packet the packet size is approx 11cm in length x 4cm We want to use the color of the image attached for the package and cornflower blue for our name Zentharo. We also need to mention close to our name....... maintaining relationships with increased libido and desire ...... Our tablets are in a tamper-proof blister pack inserted into the package. We do not have a logo as yet, we are thinking of zen in small white letters and then THARO in large letters in cornflower blue or something a bit darker. (The O could also contain a smiley face) We are not that fussed with a logo as yet, maybe down the track if our product works and sells. As of today business in Australia has ground to a halt with this coronavirus and its as bad as you could imagine. Please help us make this new product work with a fabulous packet design.
Target Market(s)
females and males
Industry/Entity Type
Pharmaceutical
Requirements
Must have
- the colors of the images attached and cornflower blue

```html
<!DOCTYPE html>
<html lang="en">
<head>
<meta charset="utf-8">
<title>Zentharo Packaging – Front Panel</title>
<link href="https://fonts.googleapis.com/css2?family=Barlow+Semi+Condensed:wght@700&family=Lato:wght@400;900&display=swap" rel="stylesheet">
<style>
  :root {
    --page-bg: #3a3a3c;
    --pack-blue: #29a3d6;
    --pack-blue-deep: #2391c2;
    --pack-blue-light: #36addf;
    --cornflower-dark: #16669a;
    --white: #ffffff;
  }
  * { box-sizing: border-box; margin: 0; padding: 0; }
  html, body {
    width: 1189px;
    height: 1200px;
    overflow: hidden;
    background: var(--page-bg);
  }
  .pack-front {
    position: absolute;
    left: 40px;
    top: 398px;
    width: 1109px;
    height: 404px;
    background: var(--pack-blue);
    overflow: hidden;
  }
  .pack-pattern {
    position: absolute;
    inset: 0;
    background:
      linear-gradient(155deg, var(--pack-blue-light) 0%, var(--pack-blue) 30%, var(--pack-blue-deep) 60%, var(--pack-blue) 100%);
    opacity: 0.9;
  }
  .dosage {
    position: absolute;
    top: 44px;
    right: 28px;
    width: 313px;
    text-align: right;
    font-family: "Barlow Semi Condensed", sans-serif;
    font-weight: 700;
    font-size: 24px;
    line-height: 1;
    color: var(--white);
    letter-spacing: 0.5px;
  }
  .dosage-rule {
    position: absolute;
    top: 80px;
    right: 28px;
    width: 313px;
    height: 4px;
    background: var(--white);
  }
  .brand-prefix {
    position: absolute;
    top: 160px;
    right: 780px;
    font-family: "Lato", sans-serif;
    font-weight: 900;
    font-size: 76px;
    line-height: 1;
    color: var(--white);
  }
  .brand-rule {
    position: absolute;
    top: 257px;
    left: 144px;
    width: 185px;
    height: 3px;
    background: var(--white);
  }
  .tagline {
    position: absolute;
    top: 266px;
    right: 780px;
    text-align: right;
    font-family: "Lato", sans-serif;
    font-weight: 400;
    font-size: 26px;
    line-height: 32px;
    color: var(--white);
  }
  .brand-name {
    position: absolute;
    top: 196px;
    right: 12px;
    text-align: right;
    white-space: nowrap;
    font-family: "Lato", sans-serif;
    font-weight: 900;
    font-size: 208px;
    line-height: 1;
    letter-spacing: -6px;
    color: var(--cornflower-dark);
  }
</style>
</head>
<body>
  <main class="pack-front">
    <div class="pack-pattern" role="img" aria-label="Faceted geometric triangle pattern in light and mid blue tones"></div>
    <p class="dosage">470MG | 30 SOFT CAPSULES</p>
    <div class="dosage-rule"></div>
    <p class="brand-prefix">zen</p>
    <div class="brand-rule"></div>
    <p class="tagline">maintaining<br>relationships<br>with increased<br>libido and desire</p>
    <h1 class="brand-name">THARO</h1>
  </main>
</body>
</html>
```